Professional Talent Needed Yesterday! Mesa Kin Vineyard needs 2 wine labels-both front & back

Our vineyard, QT LANTERNFIELD WINE LLC, has associated with a "Custom Crush" winery to make our wine. Our first red and white blends are finally ready to be labeled, bottled & sold (we hope)

We now need to quickly create front and back (maybe wraparound?) labels - & then electronically provide them to our Custom Crush winery, HOLLENDER WINE COMPANY.

The front label can be completely creative but the back label needs to contain both some narrative description of the wine, but also government-required disclosure information (listed below) As required by federal law, HOLLENDER WINE COMPANY must submit both the front and the back label "prototypes" to obtain "official" permission to use - prior to printing any labels.

Did I say, "time is of the essence"...we just completed our logo through
logoquarry & they provided this link & a copy of all of our files...

Thank you for professional help!

Jenna
(Jenna Lott Brisk)
QTLANTERNFIELD WINE LLC
lottbriskwine@mailvane.test
555-314-0927

Target Market(s)

intergenerational wine drinkers: "aficionados" not necessarily "connoisseurs""-both millennials as well their grandparents-those desiring to expand their wine experience to the high desert terroir in Arizona!

Font styles to use
Serif
Sans Serif
Script

Requirements
Must have
• - Modern design-elegant, bold, clean and easy to read font...
- Incorporate our new brand logo (or some variation of it) Our logo includes a "Southwest Mission Arch" type shape...
- All of the required governmental disclosures- see uploaded attachment
Nice to have
• -Most of the label elements for the red blend and the white blend are the same- both for the front and back labels- so the design/layout can be almost the same for each blend or they can be somewhat differentiated with any variation you believe would be complementary to each label-maybe inverse ideas (?)
- complete freedom with layout on both front & back label (attachments for required narrative & disclosure statements only)
- any "standard "size of labels for flexibility and ease of printing- shape/color of wine bottles still to be determined
- Our tag line and our names in script font

```html
<!DOCTYPE html>
<html lang="en">
<head>
<meta charset="utf-8">
<title>QT Lanternfield Wine – Labels</title>
<link href="https://fonts.googleapis.com/css2?family=Cinzel:wght@400;600&family=Libre+Caslon+Text:wght@400;700&family=Dancing+Script:wght@700&display=swap" rel="stylesheet">
<style>
  :root {
    --backdrop: #ebebeb;
    --paper: #ffffff;
    --ink: #231f20;
    --wine-red: #c41f30;
    --photo-sky: #c9d3de;
    --photo-wall: #a7abb0;
    --photo-ground: #4a4540;
    --photo-text: #ffffff;
  }
  * { box-sizing: border-box; margin: 0; padding: 0; }
  html, body { width: 1200px; height: 1200px; overflow: hidden; background: var(--backdrop); }
  body { position: relative; font-family: "Libre Caslon Text", Georgia, serif; color: var(--ink); }

  .label {
    position: absolute; left: 295px; width: 610px; height: 301px;
    background: var(--paper); box-shadow: 0 1px 3px rgba(0,0,0,.25); overflow: hidden;
  }
  .label--red { top: 225px; }
  .label--white { top: 642px; }

  /* Front panel */
  .front { position: absolute; left: 0; top: 0; width: 358px; height: 100%; }
  .front__brand {
    position: absolute; top: 56px; width: 100%; text-align: center;
    font-size: 18px; font-weight: 700; letter-spacing: .5px;
  }
  .front__brand-mark {
    display: block; width: 34px; height: 34px; margin: -42px auto 10px;
    border-radius: 50%; background: var(--ink);
  }
  .front__wine {
    position: absolute; top: 104px; width: 100%; text-align: center;
    font-size: 23px; letter-spacing: .5px;
  }
  .label--red .front__wine { color: var(--wine-red); }
  .label--white .front__wine { color: var(--ink); font-size: 19px; top: 109px; }
  .front__photo {
    position: absolute; left: 0; top: 132px; width: 358px; height: 169px;
    background: linear-gradient(180deg, var(--photo-sky) 0%, var(--photo-wall) 45%, #8d8f91 70%, var(--photo-ground) 100%);
    clip-path: polygon(0 25%, 25% 25%, 38% 3%, 50% 0, 62% 3%, 75% 25%, 100% 25%, 100% 100%, 0 100%);
  }
  .front__vintage {
    position: absolute; top: 257px; width: 100%; text-align: center;
    font-family: "Cinzel", serif; color: var(--photo-text);
    font-size: 14px; letter-spacing: 11px;
  }
  .front__place {
    position: absolute; top: 277px; width: 100%; text-align: center;
    font-family: "Cinzel", serif; color: var(--photo-text);
    font-size: 14px; letter-spacing: 3.5px; font-weight: 600;
  }

  /* Back panel */
  .back { position: absolute; left: 358px; top: 0; width: 252px; height: 100%; }
  .back__brand {
    position: absolute; top: 32px; width: 100%; text-align: center;
    font-size: 8.5px; font-weight: 700;
  }
  .back__brand-mark {
    display: block; width: 14px; height: 14px; margin: -17px auto 3px;
    border-radius: 50%; background: var(--ink);
  }
  .back__wine { position: absolute; top: 53px; width: 100%; text-align: center; font-size: 19px; }
  .label--red .back__wine { color: var(--wine-red); }
  .label--white .back__wine { font-size: 14px; top: 57px; }
  .back__blend { position: absolute; top: 83px; width: 100%; text-align: center; font-size: 11px; line-height: 15px; }
  .label--white .back__blend { top: 74px; }
  .back__story {
    position: absolute; left: 10px; right: 10px; top: 108px;
    text-align: center; font-size: 7.4px; line-height: 10px;
  }
  .label--white .back__story { top: 109px; }
  .back__signature {
    position: absolute; top: 163px; width: 100%; text-align: center;
    font-family: "Dancing Script", cursive; font-size: 10px;
  }
  .label--white .back__signature { top: 157px; }
  .back__producer {
    position: absolute; left: 21px; top: 186px; font-size: 8.4px; line-height: 10.5px;
  }
  .back__icons { position: absolute; left: 146px; top: 183px; display: flex; gap: 10px; }
  .back__icons svg { width: 21px; height: 21px; }
  .back__volume { position: absolute; left: 146px; top: 203px; font-size: 15px; }
  .back__abv { position: absolute; left: 146px; top: 222px; font-size: 6px; letter-spacing: .2px; }
  .back__warning {
    position: absolute; left: 19px; top: 233px; width: 214px; height: 49px;
    border: 1.2px solid var(--ink); padding: 2px 3px;
    font-size: 5.2px; line-height: 7.2px; text-align: justify; text-align-last: justify;
  }
  .back__footer {
    position: absolute; left: 19px; right: 19px; top: 289px;
    display: flex; justify-content: space-between; font-size: 6.8px;
  }
</style>
</head>
<body>

<article class="label label--red">
  <section class="front">
    <div class="front__brand"><span class="front__brand-mark"></span>QT LANTERNFIELD WINE</div>
    <h1 class="front__wine">T&amp;T RED</h1>
    <div class="front__photo" role="img" aria-label="Photograph of a white mission-style arched gateway under a blue sky"></div>
    <div class="front__vintage">2019</div>
    <div class="front__place">WILLCOX, ARIZONA</div>
  </section>
  <section class="back">
    <div class="back__brand"><span class="back__brand-mark"></span>QT LANTERNFIELD WINE</div>
    <h2 class="back__wine">T&amp;T RED</h2>
    <p class="back__blend">40% Barbera &nbsp;&nbsp;60% Sangiovese</p>
    <p class="back__story">Produced from grapes grown at a 4,300 foot elevation, these Italian varietals thrive in sandy loam, replete with nutrients that are brought to our Juniper Hollow Vineyard by Turkey Creek. Further nourishment by the monsoon climate of the high Arizona desert produces this wine’s unique characteristics. ¡Salud!</p>
    <p class="back__signature">Jenna &amp; Reid</p>
    <p class="back__producer">Produced and bottled by:<br>Hollender Wine Company,<br>Willcox, Arizona&nbsp; 85643<br>QTLWINE@mailvane.test</p>
    <div class="back__icons">
      <svg viewBox="0 0 24 24" role="img" aria-label="Pregnancy warning symbol"><circle cx="12" cy="12" r="10.5" fill="none" stroke="#231f20" stroke-width="1.6"/><line x1="5" y1="5" x2="19" y2="19" stroke="#231f20" stroke-width="1.6"/><circle cx="12" cy="7" r="1.8" fill="#231f20"/><path d="M10.5 10h3l1 4-2 1v4h-2v-5z" fill="#231f20"/></svg>
      <svg viewBox="0 0 24 24" role="img" aria-label="Recycle symbol"><circle cx="12" cy="12" r="10.5" fill="#231f20"/><path d="M7 13a5 5 0 0 1 8.5-3.5" fill="none" stroke="#fff" stroke-width="2"/><path d="M17 11a5 5 0 0 1-8.5 3.5" fill="none" stroke="#fff" stroke-width="2"/><path d="M14 7l3 2-3 2z" fill="#fff"/></svg>
    </div>
    <p class="back__volume">750 ml</p>
    <p class="back__abv">ALC 13.5% BY VOLUME</p>
    <p class="back__warning">GOVERNMENT WARNING: (1) ACCORDING TO THE SURGEON GENERAL, WOMEN SHOULD NOT DRINK ALCOHOLIC BEVERAGES DURING PREGNANCY BECAUSE OF THE RISK OF BIRTH DEFECTS. (2) CONSUMPTION OF ALCOHOLIC BEVERAGES IMPAIRS YOUR ABILITY TO DRIVE A CAR OR OPERATE MACHINERY, AND MAY CAUSE HEALTH PROBLEMS.</p>
    <div class="back__footer"><span>CONTAINS SULFITES</span><span>130 cases produced</span></div>
  </section>
</article>

<article class="label label--white">
  <section class="front">
    <div class="front__brand"><span class="front__brand-mark"></span>QT LANTERNFIELD WINE</div>
    <h1 class="front__wine">SLOW SUN WHITE</h1>
    <div class="front__photo" role="img" aria-label="Photograph of a white mission-style arched gateway under a blue sky"></div>
    <div class="front__vintage">2019</div>
    <div class="front__place">WILLCOX, ARIZONA</div>
  </section>
  <section class="back">
    <div class="back__brand"><span class="back__brand-mark"></span>QT LANTERNFIELD WINE</div>
    <h2 class="back__wine">SLOW SUN WHITE</h2>
    <p class="back__blend">30% Semillion &nbsp;30% Alvarinho<br>60% Chardonnay</p>
    <p class="back__story">This is our maiden mission into Arizona’s three century old winemaking history. We are a limited production vineyard and will present our finest results from time to time. High desert earth, intense sun and pure mountain rain combine to produce excellent grapes for our wine. ¡Salud!</p>
    <p class="back__signature">Jenna &amp; Reid</p>
    <p class="back__producer">Produced and bottled by:<br>Hollender Wine Company,<br>Willcox, Arizona&nbsp; 85643<br>QTLWINE@mailvane.test</p>
    <div class="back__icons">
      <svg viewBox="0 0 24 24" role="img" aria-label="Pregnancy warning symbol"><circle cx="12" cy="12" r="10.5" fill="none" stroke="#231f20" stroke-width="1.6"/><line x1="5" y1="5" x2="19" y2="19" stroke="#231f20" stroke-width="1.6"/><circle cx="12" cy="7" r="1.8" fill="#231f20"/><path d="M10.5 10h3l1 4-2 1v4h-2v-5z" fill="#231f20"/></svg>
      <svg viewBox="0 0 24 24" role="img" aria-label="Recycle symbol"><circle cx="12" cy="12" r="10.5" fill="#231f20"/><path d="M7 13a5 5 0 0 1 8.5-3.5" fill="none" stroke="#fff" stroke-width="2"/><path d="M17 11a5 5 0 0 1-8.5 3.5" fill="none" stroke="#fff" stroke-width="2"/><path d="M14 7l3 2-3 2z" fill="#fff"/></svg>
    </div>
    <p class="back__volume">750 ml</p>
    <p class="back__abv">ALC 13.5% BY VOLUME</p>
    <p class="back__warning">GOVERNMENT WARNING: (1) ACCORDING TO THE SURGEON GENERAL, WOMEN SHOULD NOT DRINK ALCOHOLIC BEVERAGES DURING PREGNANCY BECAUSE OF THE RISK OF BIRTH DEFECTS. (2) CONSUMPTION OF ALCOHOLIC BEVERAGES IMPAIRS YOUR ABILITY TO DRIVE A CAR OR OPERATE MACHINERY, AND MAY CAUSE HEALTH PROBLEMS.</p>
    <div class="back__footer"><span>CONTAINS SULFITES</span><span>52 cases produced</span></div>
  </section>
</article>

</body>
</html>
```